Seafood restaurant menu

I am looking for a new menu design for my cajun seafood restaurant. I want something modern and simple. Our menu is very small so just one page front and back. Preferred, menu size is (4.25"x11"), I have attach some images, but we will have more to give.
Updates

Need to give designer more time

Target Market(s)

young to middle aged customers

Industry/Entity Type

Restaurant Food industry

Colors
EB3D1F
EC4F4E
F09395
F8D3D4
FCEDEE

Requirements
Must have
• creativity and interesting
Nice to have
• I would like to see a clean and simple menu, but with good color placement and photos of the dishes

```html
<!DOCTYPE html>
<html lang="en">
<head>
<meta charset="utf-8">
<title>Dockside Crab House – Seafood Menu</title>
<link href="https://fonts.googleapis.com/css2?family=Roboto:ital,wght@0,300;0,400;0,500;0,700;0,900;1,300;1,400&display=swap" rel="stylesheet">
<style>
  :root{
    --red:#eb3d1f;
    --red-soft:#ec4f4e;
    --pink:#f09395;
    --blush:#f8d3d4;
    --ink:#161616;
    --stage:#2b2b2b;
    --paper:#ffffff;
    --dish-a:#c8432a;
    --dish-b:#7a3a1c;
  }
  *{margin:0;padding:0;box-sizing:border-box}
  html,body{width:1200px;height:1200px;overflow:hidden;background:var(--stage);font-family:"Roboto",Arial,sans-serif;color:var(--ink)}
  .page{position:absolute;top:61px;width:431px;height:1077px;background:var(--paper);overflow:hidden;box-shadow:0 6px 24px rgba(0,0,0,.45)}
  .page--front{left:138px}
  .page--back{left:625px}
  .band{position:absolute;left:0;right:0;background:var(--red)}
  .band--bottom{top:979px;bottom:0}
  .band--top{top:0;height:97px}
  .dish-photo{position:absolute;width:179px;height:136px;border-radius:4px;
    background:radial-gradient(circle at 50% 45%,#d89a4a 0%,var(--dish-a) 45%,var(--dish-b) 100%)}
  .brand{position:absolute;text-align:center;color:var(--red);font-weight:700;font-size:17px;line-height:20px}
  .brand-dot{display:block;width:46px;height:46px;border-radius:50%;background:var(--red);margin:0 auto 10px}
  .divider{position:absolute;left:183px;top:29px;width:3px;height:138px;background:var(--ink)}
  .title-kicker{position:absolute;left:208px;top:46px;font-size:38px;font-weight:300;letter-spacing:7px;color:var(--red);line-height:44px}
  .title-main{position:absolute;left:204px;top:86px;font-size:80px;font-weight:900;letter-spacing:-1px;line-height:86px;color:#000}
  .heading{position:absolute;left:0;right:0;text-align:center;color:var(--red);font-weight:700;font-size:21px;line-height:24px;letter-spacing:-.3px}
  .note{position:absolute;left:26px;right:0;font-size:12px;font-style:italic;font-weight:300;line-height:14px;color:var(--ink)}
  .dots{position:absolute;left:25px;width:383px;border-top:2px dotted #444}
  .row{position:absolute;left:27px;right:10px;height:18px;font-size:15px;line-height:18px;white-space:nowrap}
  .row .code{display:inline-block;width:28px}
  .row .price{position:absolute;left:266px;top:0}
  .row--back{left:26px}
  .row--back .code{width:27px}
  .row--back .price{left:318px}
  .row--plate .price{left:auto;right:0}
  .row small{font-size:12px}
  .detail{position:absolute;left:26px;right:10px;font-size:12px;font-weight:300;line-height:14px;white-space:nowrap}
  .detail--indent{left:55px}
  .frame{position:absolute;border:2px solid var(--red);border-radius:6px}
  .pill{position:absolute;background:var(--red);color:#fff;font-weight:700;font-size:20px;line-height:24px;text-align:center;border-radius:6px}
  .flavor-box{left:25px;top:845px;width:241px;height:209px}
  .sub-head{position:absolute;left:3px;color:var(--red);font-weight:700;font-size:16px;line-height:18px;letter-spacing:-.3px}
  .flavor{position:absolute;font-size:13.5px;line-height:16px;white-space:nowrap}
  .flavor::before{content:"";display:inline-block;width:6px;height:6px;border-radius:50%;background:var(--red);margin-right:7px;vertical-align:2px}
  .plain{position:absolute;left:3px;right:6px;font-size:12px;line-height:14px;white-space:nowrap}
  .plain .price{position:absolute;right:0}
</style>
</head>
<body>

<section class="page page--front">
  <div class="brand" style="left:20px;top:36px;width:144px"><span class="brand-dot"></span>Dockside Crab<br>House</div>
  <div class="divider"></div>
  <div class="title-kicker">SEAFOOD</div>
  <div class="title-main">MENU</div>

  <h2 class="heading" style="top:205px">Appetizer.</h2>
  <div class="dots" style="top:237px"></div>
  <div class="row" style="top:244px"><span class="code">A1.</span>8pc. Wings<span class="price">14/8pc.</span></div>
  <div class="detail detail--indent" style="top:269px">(Honey Lemon Pepper/Buffalo/Dockside Bomb)</div>
  <div class="row" style="top:293px"><span class="code">A2.</span>Garlic Noodles<span class="price">7</span></div>

  <h2 class="heading" style="top:331px">Fried Seafood Baskets:</h2>
  <div class="note" style="top:361px">(All baskets served with a side. Sweet Potato Fries or Hush Puppies +1)</div>
  <div class="dots" style="top:382px"></div>
  <div class="row" style="top:390px"><span class="code">F1.</span>Fried Oysters<span class="price">12</span></div>
  <div class="row" style="top:417px"><span class="code">F2.</span>Fried Shrimp<span class="price">13</span></div>
  <div class="row" style="top:444px"><span class="code">F3.</span>Fried Catfish<span class="price">12</span></div>
  <div class="row" style="top:470px"><span class="code">F4.</span>Fried Calamari<span class="price">12</span></div>
  <div class="row" style="top:497px"><span class="code">F5.</span>Soft Shell Crab *<span class="price">15</span></div>

  <h2 class="heading" style="top:540px">Sides:</h2>
  <div class="dots" style="top:569px"></div>
  <div class="row" style="top:577px"><span class="code">S1.</span>Cajun Fries<span class="price">5</span></div>
  <div class="row" style="top:604px"><span class="code">S2.</span>Sweet Potato Fries<span class="price">6</span></div>
  <div class="row" style="top:630px"><span class="code">S3.</span>Hush Puppies<span class="price">6</span></div>
  <div class="row" style="top:657px"><span class="code">S4.</span>Coleslaw<span class="price">4</span></div>
  <div class="row" style="top:684px"><span class="code">S5.</span>Steamed Rice<span class="price">3</span></div>

  <div class="frame" style="left:24px;top:738px;width:384px;height:163px"></div>
  <div class="pill" style="left:165px;top:726px;width:104px">Extras:</div>
  <div class="row" style="top:768px"><span class="code">E1.</span>Potatoes (3pc)<span class="price">$ 3</span></div>
  <div class="row" style="top:795px"><span class="code">E2.</span>Corn on the cob(2pc)<span class="price">$ 3</span></div>
  <div class="row" style="top:821px"><span class="code">E3.</span>Boiled Eggs (2pc)<span class="price">$ 3</span></div>
  <div class="row" style="top:848px"><span class="code">E4.</span>Sausage<span class="price">$ 5½ LB / $9 1Lb</span></div>
  <div class="row" style="top:875px"><span class="code">E5.</span>Sauce<span class="price">$ 6/Cup</span></div>

  <div class="band band--bottom"></div>
  <div class="dish-photo" style="left:31px;top:913px" role="img" aria-label="Photo of a seafood boil with snow crab legs, shrimp and corn"></div>
  <div class="dish-photo" style="left:221px;top:913px" role="img" aria-label="Photo of a seafood boil with snow crab legs, shrimp and corn"></div>
</section>

<section class="page page--back">
  <div class="band band--top"></div>
  <div class="dish-photo" style="left:31px;top:30px" role="img" aria-label="Photo of a seafood boil with snow crab legs, shrimp and corn"></div>
  <div class="dish-photo" style="left:221px;top:30px" role="img" aria-label="Photo of a seafood boil with snow crab legs, shrimp and corn"></div>

  <div class="frame" style="left:23px;top:192px;width:384px;height:243px"></div>
  <div class="pill" style="left:116px;top:179px;width:202px">Seafood by the LB:</div>
  <div class="row row--back" style="top:223px"><span class="code">L1.</span>Crawfish<span class="price">18</span></div>
  <div class="row row--back" style="top:250px"><span class="code">L2.</span>Shrimp w/ head<span class="price">18</span></div>
  <div class="row row--back" style="top:276px"><span class="code">L3.</span>Shrimp w/o head deveined<span class="price">20</span></div>
  <div class="row row--back" style="top:303px"><span class="code">L4.</span>Clams<span class="price">18</span></div>
  <div class="row row--back" style="top:330px"><span class="code">L5.</span>Mussels<span class="price">18</span></div>
  <div class="row row--back" style="top:356px"><span class="code">L6.</span>Snow Crab legs<span class="price">39</span></div>
  <div class="row row--back" style="top:383px"><span class="code">L7.</span>Lobster tail<span class="price">Seasonal</span></div>
  <div class="row row--back" style="top:410px"><span class="code">L8.</span>King Crab Legs<span class="price">Seasonal</span></div>

  <h2 class="heading" style="top:451px">Seafood Plates:</h2>
  <div class="note" style="top:480px">(All plates come with 1 flavor, 1 Corn, Sausages, and 1 Potato)</div>
  <div class="dots" style="left:26px;top:503px"></div>
  <div class="row row--back row--plate" style="top:511px"><span class="code">P1.</span>Seafood plate 2 LB <small>(1 flavor)</small><span class="price">$ 38</span></div>
  <div class="detail" style="top:533px">2LB Choice of Shrimp/Clams/Mussel/Crawfish</div>
  <div class="row row--back row--plate" style="top:561px"><span class="code">P3.</span>Snow Crab plate<span class="price">$ 58</span></div>
  <div class="detail" style="top:583px">1LB Snow Crab and 1LB Choice of Shrimp/Clams/Mussel/Crawfish</div>

  <h2 class="heading" style="top:620px">Family Meals:</h2>
  <div class="note" style="top:652px">(All plates come with 1 flavor, 1 Corn, Sausages, and 1 Potato)</div>
  <div class="dots" style="left:26px;top:673px"></div>
  <div class="row row--back row--plate" style="top:680px"><span class="code">M1.</span>Seafood Combo&nbsp; 3 LB <small>(1 flavor)</small><span class="price">$ 60</span></div>
  <div class="detail" style="top:702px">Choice of Shrimp/Clams/Mussel/Crawfish, ½ LB Sausage, 2 Corns, 2</div>
  <div class="detail" style="top:721px">Potato, 2 Eggs, (2cups) Fountain Soda</div>
  <div class="detail" style="top:742px">(Substitute 1LB for Snow Crab + 20)</div>
  <div class="row row--back row--plate" style="top:773px"><span class="code">M2.</span>Snow Crab Deluxe 4 LB <small>(1 flavor)</small><span class="price">$ 130</span></div>
  <div class="detail" style="top:795px">6 clusters of Snow Crab (3LB), 1LB choice of Shrimp/Clams/Mussel/</div>
  <div class="detail" style="top:814px">Crawfish, 1LB Sausage, 4 Corns, 4 Potato, 4 Eggs, (2cups) Fountain Soda</div>

  <div class="frame flavor-box">
    <div class="sub-head" style="top:4px">Choose your flavor.</div>
    <div class="flavor" style="left:3px;top:31px">Cajun (classic)</div>
    <div class="flavor" style="left:123px;top:31px">Garlic Butter</div>
    <div class="flavor" style="left:3px;top:53px">Lemon Pepper</div>
    <div class="flavor" style="left:123px;top:53px">Dockside Bomb</div>
    <div class="sub-head" style="top:84px">Spice it up:</div>
    <div class="plain" style="top:110px">Non-Spicy / Mild / Medium /Hot</div>
    <div class="sub-head" style="top:142px">Drinks:</div>
    <div class="plain" style="top:167px">Cola/Diet Cola/Zero Cola/Lemon-Lime</div>
    <div class="plain" style="top:189px">20oz Fountain (Free Refill)<span class="price">3</span></div>
  </div>

  <div class="brand" style="left:276px;top:940px;width:130px"><span class="brand-dot"></span>Dockside Crab<br>House</div>
</section>

</body>
</html>
```